Business Cards

Business cards (double-sided) to be handed out to clients and potential clients, with contact details, logo .

Target Market(s)

Small to medium size businesses

Industry/Entity Type

Accountants

Contact Information for Business Card

Brightwater Ledger & Counsel Ltd

Colors

Designer to choose only greyscale colors for use in the design.

Requirements
Must have
• Name, Title, Address, Phone number, Email, Website
Nice to have
• Modern, clean lines, classy
Should not have
• Business cards to be double-sided. Form keeps reverting to single-sided.

```html
<!DOCTYPE html>
<html lang="en">
<head>
<meta charset="utf-8">
<title>Brightwater Ledger &amp; Counsel – Business Cards</title>
<link href="https://fonts.googleapis.com/css2?family=Montserrat:wght@400;500&family=Oswald:wght@500&display=swap" rel="stylesheet">
<style>
  :root {
    --canvas: #141414;
    --card: #222222;
    --card-edge: #2c2c2c;
    --silver: #d9d9d9;
    --silver-soft: #bdbdbd;
    --rule: #8a8a8a;
  }
  * { margin: 0; padding: 0; box-sizing: border-box; }
  html, body {
    width: 1200px; height: 900px; overflow: hidden;
    background: var(--canvas);
  }
  .canvas {
    position: relative; width: 1200px; height: 900px;
    background: radial-gradient(ellipse at 60% 40%, #1e1e1e 0%, var(--canvas) 70%);
  }
  .card {
    position: absolute; left: 280px; width: 640px; height: 366px;
    background: linear-gradient(135deg, #1c1c1c 0%, var(--card) 55%, #2a2a2a 100%);
    border: 1px solid var(--card-edge);
    box-shadow: 0 14px 30px rgba(0,0,0,0.55);
  }
  .card--front { top: 62px; }
  .card--back { top: 470px; }

  .brand {
    position: absolute; inset: 0;
    display: flex; align-items: center; justify-content: center; gap: 16px;
  }
  .brand__mark {
    width: 18px; height: 18px; background: var(--silver);
  }
  .brand__name {
    font-family: "Montserrat", sans-serif; font-weight: 400;
    font-size: 27px; letter-spacing: 3px; text-transform: uppercase;
    color: var(--silver);
  }

  .holder {
    position: absolute; top: 128px; right: 362px; text-align: right;
  }
  .holder__name {
    font-family: "Oswald", sans-serif; font-weight: 500;
    font-size: 40px; line-height: 1; letter-spacing: 0.5px;
    text-transform: uppercase; color: var(--silver);
  }
  .holder__title {
    margin-top: 8px;
    font-family: "Montserrat", sans-serif; font-weight: 400;
    font-size: 16px; letter-spacing: 1px; text-transform: uppercase;
    color: var(--silver-soft);
  }
  .divider {
    position: absolute; left: 302px; top: 110px; width: 1px; height: 130px;
    background: var(--rule);
  }
  .contact {
    position: absolute; left: 326px; top: 106px;
    font-family: "Montserrat", sans-serif; font-weight: 400;
    font-size: 16px; line-height: 24px; color: var(--silver);
    list-style: none;
  }
  .contact__item { display: flex; align-items: center; gap: 8px; white-space: nowrap; }
  .contact__icon { width: 13px; height: 13px; flex: none; }
  .contact__item--plain { padding-left: 0; }
</style>
</head>
<body>
<main class="canvas">
  <section class="card card--front" aria-label="Card front">
    <div class="brand">
      <span class="brand__mark" aria-hidden="true"></span>
      <span class="brand__name">Brightwater Ledger &amp; Counsel</span>
    </div>
  </section>

  <section class="card card--back" aria-label="Card back">
    <div class="holder">
      <p class="holder__name">Daniel Hart</p>
      <p class="holder__title">Director</p>
    </div>
    <span class="divider" aria-hidden="true"></span>
    <ul class="contact">
      <li class="contact__item contact__item--plain">Suite 2140 PMB 48213</li>
      <li class="contact__item contact__item--plain">Duluth, MN 55802</li>
      <li class="contact__item">
        <svg class="contact__icon" viewBox="0 0 24 24" aria-hidden="true"><path fill="#d9d9d9" d="M6.6 10.8a15.1 15.1 0 0 0 6.6 6.6l2.2-2.2a1 1 0 0 1 1-.25 11.4 11.4 0 0 0 3.6.57 1 1 0 0 1 1 1V20a1 1 0 0 1-1 1A17 17 0 0 1 3 4a1 1 0 0 1 1-1h3.5a1 1 0 0 1 1 1c0 1.25.2 2.45.57 3.57a1 1 0 0 1-.25 1z"/></svg>
        (218) 555-0147
      </li>
      <li class="contact__item">
        <svg class="contact__icon" viewBox="0 0 24 24" aria-hidden="true"><rect x="2.5" y="5" width="19" height="14" fill="none" stroke="#d9d9d9" stroke-width="2"/><path d="M3 6l9 7 9-7" fill="none" stroke="#d9d9d9" stroke-width="2"/></svg>
        hello@brightwaterledger.com
      </li>
      <li class="contact__item">
        <svg class="contact__icon" viewBox="0 0 24 24" aria-hidden="true"><g fill="none" stroke="#d9d9d9" stroke-width="2"><circle cx="12" cy="12" r="9.5"/><ellipse cx="12" cy="12" rx="4" ry="9.5"/><path d="M2.5 12h19"/></g></svg>
        brightwaterledger.com
      </li>
    </ul>
  </section>
</main>
</body>
</html>
```